Vesit cards for web development company

We need a business card design for our company. The company develops online platforms and conducts marketing consulting. Company logo. The cards must fit in with us (a junior start UP), but they must also be professional enough to impress with investors like banks. We wish you a combination of classic and modern design

Target Market(s)

Business partners and IT and marketing customers

Industry/Entity Type

It Company

Contact Information for Business Card

Folgende Information Lena Hartwig.
Name, Position, Telefon Nr., Mobile Nr., E-Mail adresse, Optional sind noch Webadresse und HRB Nummer

Colors

Designer to choose colors to be used in the design.

Requirements
Must have
• The cards have to fit into the logo later and have to be dynamic and serious at the same time

```html
<!DOCTYPE html>
<html lang="en">
<head>
<meta charset="utf-8">
<title>Kestrel Development – Business Cards</title>
<link href="https://fonts.googleapis.com/css2?family=Open+Sans:wght@400;600;700&display=swap" rel="stylesheet">
<style>
  :root {
    --page-bg: #0b0b0b;
    --card-bg: #1c1c1d;
    --card-bg-light: #232324;
    --card-edge: #2a2a2b;
    --brand-blue: #2a7dc2;
    --text-light: #b9b9bb;
    --text-muted: #8d8d90;
  }
  * { margin: 0; padding: 0; box-sizing: border-box; }
  html, body {
    width: 1200px;
    height: 1000px;
    overflow: hidden;
    background: var(--page-bg);
    font-family: "Open Sans", Arial, sans-serif;
  }
  .stage {
    position: relative;
    width: 1200px;
    height: 1000px;
    display: flex;
    align-items: center;
    justify-content: center;
    gap: 44px;
  }
  .card {
    position: relative;
    width: 540px;
    height: 320px;
    border-radius: 22px;
    background: radial-gradient(ellipse at 40% 35%, var(--card-bg-light), var(--card-bg) 70%);
    border: 1px solid var(--card-edge);
    box-shadow: 0 18px 40px rgba(0, 0, 0, 0.6);
    overflow: hidden;
  }

  /* Wordmark */
  .wordmark {
    display: flex;
    align-items: center;
    gap: 10px;
    color: var(--brand-blue);
    font-weight: 700;
    text-transform: uppercase;
    letter-spacing: 0.02em;
    line-height: 1.05;
  }
  .wordmark__name { display: block; }
  .wordmark__name span { display: block; }
  .wordmark__dot {
    flex: none;
    border-radius: 50%;
    background: var(--brand-blue);
  }

  /* Front: contact side */
  .card--front .holder {
    position: absolute;
    left: 40px;
    top: 44px;
  }
  .holder__name {
    font-size: 20px;
    font-weight: 700;
    color: var(--text-light);
  }
  .holder__name .surname { color: var(--brand-blue); }
  .holder__role {
    font-size: 14px;
    color: var(--text-muted);
    margin-top: 2px;
  }
  .contact-list {
    list-style: none;
    position: absolute;
    left: 40px;
    top: 126px;
  }
  .contact-list li {
    display: flex;
    align-items: center;
    gap: 10px;
    font-size: 13.5px;
    color: var(--text-light);
    line-height: 1.6;
  }
  .contact-list svg { width: 12px; height: 12px; fill: var(--brand-blue); flex: none; }
  .contact-list .gap-before { margin-top: 10px; }

  .card--front .wordmark {
    position: absolute;
    right: 40px;
    top: 92px;
    font-size: 24px;
  }
  .card--front .wordmark__dot { width: 20px; height: 20px; }

  .company-meta {
    position: absolute;
    right: 40px;
    bottom: 34px;
    text-align: right;
    font-size: 14px;
    color: var(--text-light);
    line-height: 1.5;
  }

  /* Back: brand side */
  .card--back .wordmark {
    position: absolute;
    left: 50%;
    top: 50%;
    transform: translate(-50%, -50%);
    font-size: 40px;
    white-space: nowrap;
  }
  .card--back .wordmark__dot { width: 30px; height: 30px; }
</style>
</head>
<body>
<main class="stage">

  <section class="card card--front" aria-label="Business card front with contact details">
    <div class="holder">
      <p class="holder__name">Lena <span class="surname">Hartwig</span></p>
      <p class="holder__role">Manager</p>
    </div>

    <ul class="contact-list">
      <li>
        <svg viewBox="0 0 24 24" aria-hidden="true"><path d="M6.6 10.8a15.1 15.1 0 0 0 6.6 6.6l2.2-2.2a1 1 0 0 1 1-.25 11.4 11.4 0 0 0 3.6.57 1 1 0 0 1 1 1V20a1 1 0 0 1-1 1A17 17 0 0 1 3 4a1 1 0 0 1 1-1h3.5a1 1 0 0 1 1 1c0 1.25.2 2.45.57 3.6a1 1 0 0 1-.25 1z"/></svg>
        +61 2480 913
      </li>
      <li>
        <svg viewBox="0 0 24 24" aria-hidden="true"><path d="M7 1h10a2 2 0 0 1 2 2v18a2 2 0 0 1-2 2H7a2 2 0 0 1-2-2V3a2 2 0 0 1 2-2zm0 3v15h10V4z"/></svg>
        +61 4172 608
      </li>
      <li class="gap-before">
        <svg viewBox="0 0 24 24" aria-hidden="true"><path d="M2 5h20v14H2zm2 2v.5l8 5 8-5V7z"/></svg>
        lena.hartwig@kestreldev.com
      </li>
      <li>
        <svg viewBox="0 0 24 24" aria-hidden="true"><path d="M2 5h20v14H2zm2 2v.5l8 5 8-5V7z"/></svg>
        office@kestreldev.com
      </li>
    </ul>

    <div class="wordmark">
      <span class="wordmark__dot" aria-hidden="true"></span>
      <span class="wordmark__name"><span>Kestrel</span><span>Development</span></span>
    </div>

    <div class="company-meta">
      <p>HRB number - 40817</p>
      <p>www.kestreldev.com</p>
    </div>
  </section>

  <section class="card card--back" aria-label="Business card back with company name">
    <div class="wordmark">
      <span class="wordmark__dot" aria-hidden="true"></span>
      <span class="wordmark__name"><span>Kestrel</span><span>Development</span></span>
    </div>
  </section>

</main>
</body>
</html>
```